Poster - to Promote Study Skills

I have written a book about study skills for students. I want to move to using the book to give presentations. This poster looks to emphasise the fact that time is not the most important element of creating study impact, it is the intensity of the effort. The steps outline the increasing effectiveness of a study effort. The highest steps are the most effective. I have done a very rough design. It was written in the excel document, and there is a screen shot of it in the word document. I have done it is landscape, however I think it might be more effective in a portrait format.

Target Market(s)

Students aged 13 to 21

Requirements
Must have
• The 'steps' included in the files
Nice to have
• Would like to have design features, maybe colours, that support the fact that the higher 'study steps' are better.

```html
<!DOCTYPE html>
<html lang="en">
<head>
<meta charset="utf-8">
<title>Your Study Impact = Intensity of Effort x Time</title>
<link href="https://fonts.googleapis.com/css2?family=Fira+Sans:wght@900&family=Fira+Sans+Condensed:ital,wght@0,300;0,400;1,300;1,400&family=Ubuntu:wght@400;500&display=swap" rel="stylesheet">
<style>
  :root {
    --ink: #1d1d1f;
    --paper: #f6f6f7;
    --swoosh: #e4e4e6;
    --blue-deep: #0a6fc4;
    --blue-mid: #049fe0;
    --blue-light: #35c3f2;
    --rail: #3a3a3c;
    --step60-a: #00eaa8; --step60-b: #00b2a0; --dot60: #00c997;
    --step50-a: #9b96e8; --step50-b: #7a6ba8; --dot50: #8d86d3;
    --step40-a: #35d3fd; --step40-b: #0787fb; --dot40: #1eb3fb;
    --step30-a: #fe4d89; --step30-b: #da0550; --dot30: #ea1c69;
    --step20-a: #ff7900; --step20-b: #ff4a04; --dot20: #ff6000;
    --step10-a: #fedb2e; --step10-b: #ff9711; --dot10: #ffc61c;
  }
  * { margin: 0; padding: 0; box-sizing: border-box; }
  html, body { width: 849px; height: 1200px; overflow: hidden; background: #fff; }
  .poster {
    position: relative; width: 849px; height: 1200px; overflow: hidden;
    background: var(--paper); color: var(--ink);
    font-family: "Fira Sans Condensed", "Arial Narrow", sans-serif;
  }
  .backdrop, .header-wave { position: absolute; left: 0; top: 0; }
  .title {
    position: absolute; top: 24px; left: 0; width: 849px; text-align: center;
    font-family: "Fira Sans", sans-serif; font-weight: 900; font-size: 29.5px;
    letter-spacing: 0.6px; color: #fff; white-space: nowrap;
  }
  .subtitle {
    position: absolute; top: 66px; left: 0; width: 849px; text-align: center;
    font-style: italic; font-weight: 300; font-size: 25px; color: #fff;
    letter-spacing: 0.1px; white-space: nowrap;
  }
  .quote { position: absolute; font-style: italic; font-weight: 300; font-size: 21px; line-height: 25.5px; }
  .quote p { margin-bottom: 24px; }
  .quote cite { display: block; font-style: normal; font-weight: 400; font-variant: small-caps; font-size: 20px; letter-spacing: 0.2px; }
  .quote-commitment { left: 21px; top: 208px; width: 380px; }
  .quote-habit { left: 425px; top: 208px; width: 385px; text-align: right; }
  .quote-habit p { margin-bottom: 21px; padding-right: 2px; }
  .quote-habit cite { text-align: left; }
  .quote-focus { left: 17px; top: 399px; width: 280px; }
  .hero-figure {
    position: absolute; left: 22px; top: 552px; width: 205px; height: 390px;
    border-radius: 45% 55% 40% 60% / 30% 30% 70% 70%;
    background: linear-gradient(160deg, #ff9f6b 0%, #2aa9f0 30%, #1b8fe0 55%, #e8346f 80%, #8f1c2a 100%);
    opacity: .9;
  }
  .step {
    position: absolute; height: 117px; border-radius: 18px; color: #fff;
    font-family: "Ubuntu", sans-serif; display: flex;
  }
  .step-title {
    display: flex; flex-direction: column; justify-content: center;
    font-weight: 500; font-size: 16px; line-height: 20.5px; padding-left: 12px;
    white-space: nowrap; border-right: 2px solid rgba(255,255,255,.95);
    margin: 10px 0;
  }
  .step-desc { font-size: 12px; line-height: 15.4px; padding: 17px 14px 0 9px; }
  .step-60 { left: 316px; top: 405px; width: 501px; background: linear-gradient(90deg, var(--step60-a), var(--step60-b)); }
  .step-60 .step-title { width: 201px; }
  .step-50 { left: 264px; top: 537px; width: 553px; background: linear-gradient(90deg, var(--step50-a), var(--step50-b)); }
  .step-50 .step-title { width: 201px; }
  .step-50 .step-desc { padding-top: 27px; }
  .step-40 { left: 217px; top: 669px; width: 600px; background: linear-gradient(90deg, var(--step40-a), var(--step40-b)); }
  .step-40 .step-title { width: 204px; padding-left: 15px; }
  .step-30 { left: 163px; top: 800px; width: 654px; background: linear-gradient(90deg, var(--step30-a), var(--step30-b)); }
  .step-30 .step-title { width: 199px; }
  .step-30 .step-desc { padding-top: 14px; }
  .step-20 { left: 100px; top: 932px; width: 718px; background: linear-gradient(90deg, var(--step20-a), var(--step20-b)); }
  .step-20 .step-title { width: 215px; padding-left: 27px; }
  .step-20 .step-desc { padding-top: 35px; }
  .step-10 { left: 35px; top: 1064px; width: 783px; background: linear-gradient(90deg, var(--step10-a), var(--step10-b)); }
  .step-10 .step-title { width: 225px; padding-left: 27px; }
  .step-10 .step-desc { padding-top: 42px; }
  .progress-rail { position: absolute; left: 0; top: 0; }
</style>
</head>
<body>
<main class="poster">
  <svg class="backdrop" width="849" height="1200" viewBox="0 0 849 1200" aria-hidden="true">
    <path d="M0 400 C 180 420, 330 520, 400 700 L 640 1200 L 0 1200 Z" fill="#ebebec"/>
    <path d="M390 120 C 470 300, 560 500, 700 880 L 760 1200 L 600 1200 C 560 900, 480 600, 340 300 Z" fill="var(--swoosh)" opacity=".8"/>
  </svg>
  <svg class="header-wave" width="849" height="200" viewBox="0 0 849 200" aria-hidden="true">
    <defs>
      <linearGradient id="waveMain" x1="0" y1="0" x2="1" y2="0">
        <stop offset="0" stop-color="var(--blue-mid)"/>
        <stop offset=".6" stop-color="var(--blue-deep)"/>
        <stop offset="1" stop-color="var(--blue-deep)"/>
      </linearGradient>
    </defs>
    <path d="M0 0 H849 V150 C 780 120, 700 90, 600 100 C 420 120, 220 190, 0 172 Z" fill="var(--blue-light)"/>
    <path d="M0 0 H849 V40 C 700 60, 560 70, 440 95 C 280 130, 140 175, 0 172 Z" fill="url(#waveMain)"/>
    <path d="M0 0 H420 C 300 40, 150 90, 0 110 Z" fill="#04a6e6" opacity=".7"/>
  </svg>

  <h1 class="title">YOUR STUDY IMPACT = INTENSITY OF EFFORT X TIME</h1>
  <p class="subtitle">THE FORMULA FOR BANKING HIGH PERFORMANCE STUDY IMPACTS</p>

  <blockquote class="quote quote-commitment">
    <p>"There are only two option regarding commitment. You are either in or you are out. There is no such thing as life in-between."</p>
    <cite>Dale Morrow, Pro Basketball Coach</cite>
  </blockquote>
  <blockquote class="quote quote-habit">
    <p>"We are what we repeatedly do. Excellence,then,is not an act but a habit."</p>
    <cite>Edwin Harlow, American Writer <i>and Philosopher</i></cite>
  </blockquote>
  <blockquote class="quote quote-focus">
    <p>"Success in anything will always come down to this: Focus and Effort, and we control both ofthem."</p>
    <cite>Marcus "The Anvil" Reed</cite>
  </blockquote>

  <div class="hero-figure" role="img" aria-label="Illustration of a graduate in cap, gown and cape flying upward with one arm raised"></div>

  <section class="step step-60">
    <h2 class="step-title"><span>$60 an Hour Study Effort</span><span>The Aspirational Step</span></h2>
    <p class="step-desc">Flow - 'In the zone' - easy, productive study<br>Purpose, intent, focus, stress control, positive mindset</p>
  </section>
  <section class="step step-50">
    <h2 class="step-title"><span>$50 an Hour Study Effort</span><span>Balance and Health</span></h2>
    <p class="step-desc">Study is supported by positive social, recreational and health habits - balance in life<br>(exercise and healthy eating) and community engagement</p>
  </section>
  <section class="step step-40">
    <h2 class="step-title"><span>$40 an Hour Study Effort</span><span>Studing Smarter</span></h2>
    <p class="step-desc">Using effective study techniques - graphic organisers; practice questions; reflecting on study progress; hand writing notes short, sharp, distraction free periods of effort (pomodoro method), learning from feedback, spaced revision</p>
  </section>
  <section class="step step-30">
    <h2 class="step-title"><span>$30 an Hour Study Effort</span><span>The Right State of Mind</span></h2>
    <p class="step-desc">Positive mindset toward the learning (self-directed, setting goals, enthusiastic about challenge)<br>Planning of assignment efforts/revising between learning and the exam - moving away from relying on the last minute and challenging procrastination<br>Adequate sleep with good sleep habits</p>
  </section>
  <section class="step step-20">
    <h2 class="step-title"><span>$20 an Hour Study Effort</span><span>Single Tasking</span></h2>
    <p class="step-desc">The study environment is free of distractions (quiet, no phone, no TV, no social media, no email, no music with lyrics)<br>with good organisation (eg effective homework diary use)</p>
  </section>
  <section class="step step-10">
    <h2 class="step-title"><span>$10 an Hour Study Effort</span><span>Building a Foundation</span></h2>
    <p class="step-desc">Study time is supported by engagement in class</p>
  </section>

  <svg class="progress-rail" width="849" height="1200" viewBox="0 0 849 1200" aria-hidden="true">
    <line x1="831" y1="370" x2="831" y2="1180" stroke="var(--rail)" stroke-width="2"/>
    <path d="M824 376 L831 357 L838 376 Z" fill="var(--rail)"/>
    <circle cx="831" cy="465" r="10" fill="var(--dot60)"/>
    <circle cx="831" cy="595" r="10" fill="var(--dot50)"/>
    <circle cx="831" cy="724" r="10" fill="var(--dot40)"/>
    <circle cx="831" cy="857" r="10" fill="var(--dot30)"/>
    <circle cx="831" cy="991" r="10" fill="var(--dot20)"/>
    <circle cx="831" cy="1121" r="10" fill="var(--dot10)"/>
  </svg>
</main>
</body>
</html>
```